依頼詳細
弊社オリジナルのコンセプト企画住宅をプロデュースするにあたり
お客様にお渡しする資料として使用するリーフレットの制作をお願いします。
「樹影」にはまだカタログやパンフレットが無いので、このリーフレットがお客様への最初のご案内・ご紹介になります。
記載項目
松葉建築株式会社 代表取締役 堀内宗一 お問合せ 0297-61-3027 sora@matsuba-kenchiku.jp
サイズ
A3
ページ数
両面
希望イメージ
シンプル 複雑
単色 カラフル
暗い 明るい
日常 高級
遊び心 厳粛
未来的 伝統的
女性的 男性的
希望する色
納品ファイル
• イラストレーター形式 (.ai)
補足説明
下記のフォルダに、必要なファイルを入れました。
https://files.hokuyo-share.net/f/7Qp2XkLm9RtVw4Zc8Nd3sJb6Hy1Ga5Ue?mode=view
■ 選んだ理由

ご提案いただいた中には、メッセージで協調してくれたいいご提案もあったのですが、内容ボリュームが薄い中で、内容に充実感が感じられたり、その内容とページに集中できる設計になっていたので、読んでいただけるのかなと思いまして選びました

インパクトがあったので決めました。

■ 提案者全員のお礼・コメント

皆さま、ご提案ありがとうございました。 今後もあらたなコンセプトで様々な広告をお願いしようと思っておりますので、どうぞよろしくお願いします!

```html
<!DOCTYPE html>
<html lang="ja">
<head>
<meta charset="utf-8">
<title>樹影 リーフレット</title>
<link rel="stylesheet" href="https://fonts.googleapis.com/css2?family=Shippori+Mincho:wght@400;500;600&family=Cormorant+Garamond:wght@500&family=Dancing+Script:wght@500&display=swap">
<style>
  :root {
    --paper: #f4f0ea;
    --paper-deep: #ece6dc;
    --ink: #7b7388;
    --ink-soft: #9a93a4;
    --rule: #8f889a;
    --logo-tile: #d9ddd3;
    --tag: #ffffff;
    --illo-people: #d8d3cc;
    --illo-green: #b9c6a9;
    --illo-warm: #e8c9a8;
  }
  * { margin: 0; padding: 0; box-sizing: border-box; }
  html, body { width: 851px; height: 1200px; overflow: hidden; background: var(--paper); }
  .leaflet {
    position: relative; width: 851px; height: 1200px; overflow: hidden;
    background: radial-gradient(ellipse at 50% 40%, var(--paper) 0%, var(--paper-deep) 100%);
    font-family: "Shippori Mincho", serif; color: var(--ink);
  }
  .title {
    position: absolute; left: 570px; top: 55px;
    writing-mode: vertical-rl; font-size: 78px; font-weight: 500;
    letter-spacing: 4px; color: var(--ink); line-height: 1;
  }
  .title-sub {
    position: absolute; left: 662px; top: 62px;
    writing-mode: vertical-rl; font-size: 11px; letter-spacing: 3px; color: var(--ink-soft);
  }
  .lifestyle {
    position: absolute; left: 118px; top: 155px; width: 80px;
    font-family: "Cormorant Garamond", serif; font-size: 15px; letter-spacing: 5px; color: var(--ink);
  }
  .lifestyle span { display: block; padding: 10px 0; border-bottom: 1px solid var(--rule); }
  .lifestyle span:last-child { border-bottom: none; }
  .illo { position: absolute; border-radius: 12px; }
  .illo-people { left: 300px; top: 100px; width: 250px; height: 305px; background: linear-gradient(180deg, var(--illo-people), var(--paper-deep)); }
  .illo-reader { left: 572px; top: 395px; width: 165px; height: 160px; background: linear-gradient(180deg, var(--illo-green), var(--paper-deep)); }
  .illo-garden { left: 85px; top: 470px; width: 185px; height: 185px; background: linear-gradient(180deg, var(--illo-warm), var(--illo-green)); }
  .illo-music { left: 235px; top: 690px; width: 165px; height: 155px; background: linear-gradient(180deg, var(--illo-warm), var(--paper-deep)); }
  .tag {
    position: absolute; background: var(--tag); color: var(--ink);
    font-size: 15px; letter-spacing: 2px; padding: 7px 14px;
  }
  .tag-read { left: 680px; top: 312px; transform: rotate(-28deg); }
  .tag-garden { left: 100px; top: 372px; transform: rotate(-26deg); }
  .caption-music { position: absolute; left: 265px; top: 665px; font-size: 15px; letter-spacing: 2px; }
  .logo-tile {
    position: absolute; left: 327px; top: 425px; width: 185px; height: 172px;
    background: var(--logo-tile); display: flex; align-items: center; justify-content: center;
  }
  .logo-name { color: #fff; font-family: "Cormorant Garamond", serif; font-size: 22px; letter-spacing: 3px; text-align: center; line-height: 1.3; }
  .headline {
    position: absolute; left: 572px; top: 625px;
    font-size: 38px; font-weight: 600; line-height: 1.45; letter-spacing: 3px; color: var(--ink);
  }
  .profile-head {
    position: absolute; left: 90px; top: 880px; width: 680px;
    display: flex; align-items: center; gap: 14px;
  }
  .profile-head .line { flex: 1; height: 1px; background: var(--rule); }
  .profile-head .line.short { flex: 0 0 90px; }
  .profile-head h2 { font-family: "Dancing Script", cursive; font-weight: 500; font-size: 24px; color: var(--ink); }
  .profile-cols {
    position: absolute; left: 100px; top: 925px; width: 680px;
    display: grid; grid-template-columns: repeat(3, 1fr); gap: 30px;
    font-size: 10px; line-height: 1.75; color: var(--ink);
  }
  .rule-bottom { position: absolute; left: 90px; top: 1082px; width: 690px; height: 1px; background: var(--rule); }
  .closing {
    position: absolute; left: 250px; top: 1100px; width: 540px;
    font-size: 19px; line-height: 1.95; letter-spacing: 3px; color: var(--ink);
  }
</style>
</head>
<body>
<main class="leaflet">
  <h1 class="title">樹影</h1>
  <p class="title-sub">ふたりの時間を愉しむ家</p>

  <div class="lifestyle"><span>LIFE</span><span>STYLE</span><span>IMAGE</span></div>

  <div class="illo illo-people" role="img" aria-label="並んで立つ夫婦と家族のイラスト"></div>
  <span class="tag tag-read">本を読む</span>
  <div class="illo illo-reader" role="img" aria-label="ベンチで本を読む人のイラスト"></div>

  <span class="tag tag-garden">ガーデニング</span>
  <div class="illo illo-garden" role="img" aria-label="庭で草花を育てる女性のイラスト"></div>

  <div class="logo-tile"><span class="logo-name">MATSUBA<br>KENCHIKU</span></div>

  <p class="caption-music">音楽を聴く…</p>
  <div class="illo illo-music" role="img" aria-label="音楽を聴いてくつろぐ女性のイラスト"></div>

  <p class="headline">夫婦2人<br>の生活を<br>優先した<br>平家+αの家</p>

  <div class="profile-head"><span class="line short"></span><h2>Profile</h2><span class="line"></span></div>
  <div class="profile-cols">
    <p>夫<br>年齢：40歳前後<br>職業：会社員（事務職）<br>趣味：読書・ドライブ<br>休日は静かな書斎で読書を楽しむ。<br>家では自分だけの時間が欲しい。</p>
    <p>妻<br>年齢：38歳前後<br>職業：パート勤務<br>趣味：ガーデニング・料理<br>庭で季節の花や野菜を育てたい。<br>家事動線のよい間取りが希望。</p>
    <p>娘<br>年齢：12歳<br>学年：小学6年生<br>趣味：音楽・イラスト<br>自分の部屋で音楽を聴くのが好き。<br>将来は独立を見据えた子ども部屋。</p>
  </div>
  <div class="rule-bottom"></div>

  <p class="closing">趣味や好きな事をする時、その場所で没頭でき、<br>それぞれが良い距離感を自然と保てる家。</p>
</main>
</body>
</html>
```